Bauträger  sucht Webdesign
Bauträger sucht Webdesign
Zielgruppe
Wir sind Bauträger in Öhringen und erstellen Einfamilienhäuser, Mehrfamilienhäuser und Reihenhäuser. Als LM-Hausbau gehen wir gerne auf die individuellen Wünsche unserer Kunden ein. Wir planen sowohl für die junge Familie, als auch für reifere Kunden, mit altersgerechtem Anspruch an die Hausgestaltung.
Aufgabenstellung
Unsere Homepage muss ein moderneres Escheinungsbild bekommen. Unser Logo soll als betongrau /silberne Grafik eingebunden werden. Inhaltlich soll der interessierte Besucher primär schnell eine ansprechende Auswahl haben, um seinen individuellen Vorstellungen näher zu kommen.

```html
<!DOCTYPE html>
<html lang="de">
<head>
<meta charset="utf-8">
<title>LM-Hausbau</title>
<link href="https://fonts.googleapis.com/css2?family=Lato:wght@300;400;700&display=swap" rel="stylesheet">
<style>
:root{
  --blue:#29abe2;
  --ink:#2b2b2b;
  --text:#3c3c3c;
  --muted:#8a8a8a;
  --line:#d6d6d6;
  --slate:#2c2d30;
  --slate-dark:#242528;
  --white:#ffffff;
  --icon-grey:#cfcfcf;
}
*{margin:0;padding:0;box-sizing:border-box}
html,body{width:1200px;height:3800px;overflow:hidden;background:var(--white)}
body{position:relative;font-family:'Lato',sans-serif;color:var(--text)}
h1,h2,h3{font-weight:400}
.abs{position:absolute}
.center{left:0;width:1200px;text-align:center}

/* hero */
.hero{top:0;left:0;width:1200px;height:622px;background:linear-gradient(180deg,#6f6a55 0%,#9a9684 35%,#b9b8ae 60%,#8b8a80 78%,#7a756c 100%)}
.brand{top:0;left:234px;width:81px;height:94px;background:#3a3a3a;color:var(--white);display:flex;align-items:flex-end;justify-content:center;padding-bottom:14px;font-size:13px;font-weight:700;text-align:center;line-height:1.1}
.hero-phone{top:48px;left:367px;color:var(--white);font-size:14px;display:flex;align-items:center;gap:5px}
.menu{top:32px;left:924px;width:44px}
.menu-label{top:76px;left:924px;width:44px;text-align:center;color:var(--white);font-size:11px}
.hero-title{top:138px;color:var(--white);font-size:45px;font-weight:400;line-height:57px;text-shadow:0 1px 4px rgba(0,0,0,.25)}
.catalog-btn{top:187px;left:986px;width:214px;height:44px;background:var(--blue);color:var(--white);font-size:11px;font-weight:700;display:flex;align-items:center;padding-left:22px;line-height:14px;text-align:center}
.catalog-btn svg{position:absolute;right:18px;top:12px}

/* headings */
.heading{color:var(--ink);font-weight:400}
.rule{height:3px;background:var(--blue);width:60px;left:570px}

.intro-title{top:676px;font-size:25px}
.col{font-size:11px;line-height:19px;color:var(--text);width:354px}
.col p{margin-bottom:19px}

.video{top:954px;left:0;width:1200px;height:302px;background:linear-gradient(180deg,#4a5046 0%,#6c6a60 40%,#8c8a82 60%,#3d4238 100%)}
.play{top:1072px;left:565px}

/* house types */
.types-line{top:1374px;left:0;width:1200px;height:2px;background:var(--line)}
.type{width:190px;text-align:center}
.type svg{display:block;margin:0 auto}
.type-name{font-size:19px;color:var(--ink);margin-top:12px}
.type-desc{font-size:11px;line-height:18px;color:var(--text);margin-top:3px}

/* feature */
.feature-img{top:1495px;left:0;width:600px;height:462px;background:linear-gradient(180deg,#a9c4dc 0%,#d8d7d0 40%,#b8b4a8 70%,#5f5e52 100%)}
.feature-panel{top:1495px;left:600px;width:600px;height:462px;background:var(--slate);color:var(--white)}
.feature-title{top:1538px;left:671px;font-size:18px;color:var(--white)}
.feature-text{top:1568px;left:671px;width:300px;font-size:11px;line-height:19px;color:var(--white)}
.feature-line{top:1654px;left:671px;width:529px;height:2px;background:#45474c}
.feature-line i{display:block;width:44px;height:3px;background:var(--blue)}
.spec{left:671px;width:300px;display:flex;align-items:center;font-size:11px;color:var(--white)}
.spec svg{width:26px;margin-right:8px}
.spec .k{width:94px}
.pill{height:30px;border-radius:15px;background:var(--blue);color:var(--white);font-size:11px;font-weight:700;letter-spacing:.5px;display:flex;align-items:center;justify-content:center}

/* gallery */
.gallery-title{top:2012px;font-size:25px}
.gallery-text{top:2090px;left:299px;width:602px;text-align:center;font-size:11px;line-height:19px}
.tile{height:269px}

/* appointment */
.appointment{top:2848px;left:0;width:1200px;height:240px;background:var(--slate-dark)}
.appointment-text{top:2902px;color:var(--white);font-size:31px;line-height:44px;font-weight:400}

/* contact */
.contact-title{top:3138px;font-size:37px}
.contact-sub{top:3228px;font-size:11px}
.field{font-size:17px;font-weight:300;color:#555;border-bottom:1px solid var(--line);padding-bottom:4px;height:27px}
.note{top:3480px;left:231px;font-size:10px;line-height:18px;color:var(--muted);font-weight:300}
.send{top:3566px;left:734px;width:234px;height:38px;background:var(--blue);color:var(--white);font-size:11px;font-weight:700;display:flex;align-items:center;justify-content:center;box-shadow:0 2px 4px rgba(0,0,0,.2)}
.send svg{position:absolute;right:24px;top:9px}

/* footer */
.footer{top:3653px;left:0;width:1200px;height:147px;background:var(--slate)}
.footer-col{top:3678px;color:var(--white);font-size:11px;line-height:19px}
.footer-col b{font-weight:700}
</style>
</head>
<body>

<header>
  <div class="abs hero" role="img" aria-label="Foto: Paar liegt auf einem Steg am See und hält ein Papierhaus in die Höhe"></div>
  <div class="abs brand">LM-Hausbau</div>
  <div class="abs hero-phone">
    <svg width="12" height="12" viewBox="0 0 24 24"><path d="M6.6 10.8a15 15 0 006.6 6.6l2.2-2.2c.3-.3.7-.4 1-.2 1.1.4 2.3.6 3.6.6.6 0 1 .4 1 1V20c0 .6-.4 1-1 1A17 17 0 013 4c0-.6.4-1 1-1h3.5c.6 0 1 .4 1 1 0 1.3.2 2.5.6 3.6.1.3 0 .7-.2 1z" fill="#fff"/></svg>
    07390/ 4827-0
  </div>
  <svg class="abs menu" height="32" viewBox="0 0 44 32"><path d="M2 2h42M12 13h32M2 24h42" stroke="#fff" stroke-width="2"/></svg>
  <div class="abs menu-label">MENÜ</div>
  <h1 class="abs center hero-title">Lorem ipsum dolor sit amet<br>consectetuer adipiscing elit.</h1>
  <div class="abs catalog-btn">FORDERN SIE UNSEREN<br>HAUSKATALOG AN !
    <svg width="26" height="20" viewBox="0 0 26 20"><path d="M1 10h23M15 1l9 9-9 9" stroke="#fff" stroke-width="2" fill="none"/></svg>
  </div>
</header>

<section class="intro">
  <h2 class="abs center heading intro-title">Sie wollen energiebewusst, preiswert und massiv Bauen?</h2>
  <div class="abs rule" style="top:720px"></div>
  <div class="abs col" style="top:746px;left:231px">
    <p>Lorem ipsum dolor sit amet, consectetuer adipiscing elit. Aenean commodo ligula eget dolor. Aenean massa. Cum sociis natoque penatibus et magnis dis parturient montes, nascetur ridiculus mus. Donec quam felis, ultricies nec, pellentesque eu, pretium quis, sem. Nulla consequat massa quis enim.</p>
    <p>Donec pede justo, fringilla vel, aliquet nec, vulputate eget, arcu. In enim justo, rhoncus ut, imperdiet a, venenatis vitae, justo. Nullam dictum felis</p>
  </div>
  <div class="abs col" style="top:746px;left:609px">
    <p>Lorem ipsum dolor sit amet, consectetuer adipiscing elit. Aenean commodo ligula eget dolor. Aenean massa. Cum sociis natoque penatibus et magnis dis parturient montes, nascetur ridiculus mus. Donec quam felis, ultricies nec, pellentesque eu, pretium quis, sem.</p>
    <p>Nulla consequat massa quis enim. Donec pede justo, fringilla vel, aliquet nec, vulputate eget, arcu. In enim justo, rhoncus ut, imperdiet a, venenatis vitae, justo. Nullam dictum felis eu pede mollis pretium.</p>
  </div>
</section>

<section>
  <div class="abs video" role="img" aria-label="Videovorschau: modernes Einfamilienhaus mit Terrasse und Sonnenschirm"></div>
  <svg class="abs play" width="66" height="66" viewBox="0 0 66 66"><circle cx="33" cy="33" r="31" fill="rgba(255,255,255,.15)" stroke="#29abe2" stroke-width="3"/><path d="M27 23l16 10-16 10z" fill="#fff"/></svg>
</section>

<section class="types">
  <div class="abs types-line"></div>
  <div class="abs type" style="top:1318px;left:222px">
    <svg width="64" height="46" viewBox="0 0 64 46"><path d="M4 20L32 3l28 17" stroke="#29abe2" stroke-width="5" fill="none"/><rect x="10" y="20" width="44" height="24" fill="#29abe2"/><rect x="18" y="26" width="10" height="18" fill="#fff"/><rect x="34" y="26" width="13" height="9" fill="#fff"/></svg>
    <div class="type-name">Kopenhagen</div>
    <div class="type-desc">Lorem ipsum dolor sit amet,<br>consectetuer adipiscing elit.</div>
  </div>
  <div class="abs type" style="top:1318px;left:411px">
    <svg width="64" height="46" viewBox="0 0 64 46"><path d="M4 20L32 3l28 17" stroke="#cfcfcf" stroke-width="5" fill="none"/><rect x="10" y="20" width="44" height="24" fill="#cfcfcf"/><rect x="18" y="26" width="10" height="18" fill="#fff"/><rect x="34" y="26" width="13" height="9" fill="#fff"/></svg>
    <div class="type-name">Cannes</div>
    <div class="type-desc">Lorem ipsum dolor sit amet,<br>consectetuer adipiscing elit.</div>
  </div>
  <div class="abs type" style="top:1318px;left:599px">
    <svg width="64" height="46" viewBox="0 0 64 46"><path d="M4 20L32 3l28 17" stroke="#cfcfcf" stroke-width="5" fill="none"/><rect x="10" y="20" width="44" height="24" fill="#cfcfcf"/><rect x="18" y="26" width="10" height="18" fill="#fff"/><rect x="34" y="26" width="13" height="9" fill="#fff"/></svg>
    <div class="type-name">Amsterdam</div>
    <div class="type-desc">Lorem ipsum dolor sit amet,<br>consectetuer adipiscing elit.</div>
  </div>
  <div class="abs type" style="top:1318px;left:788px">
    <svg width="64" height="46" viewBox="0 0 64 46"><path d="M4 20L32 3l28 17" stroke="#cfcfcf" stroke-width="5" fill="none"/><rect x="10" y="20" width="44" height="24" fill="#cfcfcf"/><rect x="18" y="26" width="10" height="18" fill="#fff"/><rect x="34" y="26" width="13" height="9" fill="#fff"/></svg>
    <div class="type-name">Oslo</div>
    <div class="type-desc">Lorem ipsum dolor sit amet,<br>consectetuer adipiscing elit.</div>
  </div>
</section>

<section class="feature">
  <div class="abs feature-img" role="img" aria-label="Foto: Haustyp Kopenhagen, zweigeschossiges Haus mit Holzverkleidung und Terrasse"></div>
  <div class="abs feature-panel"></div>
  <h3 class="abs feature-title">Haustyp “Kopenhagen”</h3>
  <p class="abs feature-text">Lorem ipsum dolor sit amet, consectetuer adipiscing elit. Aenean commodo ligula eget dolor. Aenean massa. Cum sociis natoque penatibus et magnis dis parturient montes.</p>
  <div class="abs feature-line"><i></i></div>
  <div class="abs spec" style="top:1703px">
    <svg height="22" viewBox="0 0 26 22"><path d="M2 20L11 4l10 16z" stroke="#29abe2" stroke-width="2" fill="none"/><rect x="11" y="8" width="13" height="12" stroke="#29abe2" stroke-width="2" fill="none"/></svg>
    <span class="k">Dachart:</span><span>Flachdach</span>
  </div>
  <div class="abs spec" style="top:1742px">
    <svg height="22" viewBox="0 0 26 22"><rect x="4" y="3" width="18" height="16" stroke="#29abe2" stroke-width="2" fill="none"/><rect x="4" y="12" width="18" height="7" fill="#29abe2"/></svg>
    <span class="k">Erdgeschoss:</span><span>122 m²</span>
  </div>
  <div class="abs spec" style="top:1780px">
    <svg height="22" viewBox="0 0 26 22"><path d="M3 19L13 3l10 16z" stroke="#29abe2" stroke-width="2" fill="none"/></svg>
    <span class="k">Dachgeschoss:</span><span>103 m²</span>
  </div>
  <div class="abs spec" style="top:1817px">
    <svg height="22" viewBox="0 0 26 22"><rect x="3" y="13" width="4" height="7" fill="#29abe2"/><rect x="9" y="10" width="4" height="10" fill="#29abe2"/><rect x="15" y="13" width="4" height="7" fill="#29abe2"/><circle cx="19" cy="6" r="4.5" fill="#29abe2"/></svg>
    <span class="k">Nutzfläche:</span><span>280 m²</span>
  </div>
  <div class="abs pill" style="top:1876px;left:672px;width:170px">MEHR ERFAHREN</div>
</section>

<section class="gallery">
  <h2 class="abs center heading gallery-title">Gallery</h2>
  <div class="abs rule" style="top:2054px"></div>
  <p class="abs gallery-text">Lorem ipsum dolor sit amet, consectetuer adipiscing elit. Aenean commodo ligula eget dolor. Aenean massa. Cum sociis natoque penatibus et magnis dis parturient montes, nascetur ridiculus mus. Donec quam felis, ultricies nec, pellentesque eu, pretium quis, sem.</p>
  <div class="abs tile" style="top:2179px;left:0;width:402px;background:linear-gradient(135deg,#e9e4dc,#b88a5c)" role="img" aria-label="Foto: Badezimmer mit Doppelwaschbecken und Pflanze"></div>
  <div class="abs tile" style="top:2179px;left:402px;width:395px;background:linear-gradient(180deg,#c9cfd6 0%,#e8e8e6 55%,#6f8a4e 100%)" role="img" aria-label="Foto: weißes Einfamilienhaus mit Garten"></div>
  <div class="abs tile" style="top:2179px;left:797px;width:403px;background:linear-gradient(135deg,#2a2a2a,#dcdcdc 60%,#f2f2f2)" role="img" aria-label="Foto: moderne Küche mit Kochinsel"></div>
  <div class="abs tile" style="top:2448px;left:0;width:402px;background:linear-gradient(135deg,#f1ede6,#c9a074)" role="img" aria-label="Foto: offener Wohnbereich mit Holztreppe"></div>
  <div class="abs tile" style="top:2448px;left:402px;width:395px;background:linear-gradient(135deg,#dfe3e6,#8d6a4d)" role="img" aria-label="Foto: Küche mit Essbereich und Wandbildern"></div>
  <div class="abs tile" style="top:2448px;left:797px;width:403px;background:linear-gradient(135deg,#cfdad6,#f3f3f3 55%,#1e1e1e)" role="img" aria-label="Foto: Badezimmer mit Glasdusche"></div>
  <div class="abs pill" style="top:2755px;left:514px;width:170px;height:31px">MEHR BILDER</div>
</section>

<section>
  <div class="abs appointment"></div>
  <p class="abs center appointment-text">Vereinbaren Sie einen Besichtigungstermin<br>in einem unserer Musterhäuser<br>Tel.: 07390/ 4827-0</p>
</section>

<section class="contact">
  <h2 class="abs center heading contact-title">Kontakt</h2>
  <div class="abs rule" style="top:3192px"></div>
  <p class="abs center contact-sub">Aenean commodo ligula eget dolor. Aenean massa. Integer tincidunt.</p>
  <div class="abs field" style="top:3289px;left:231px;width:359px">Vorname*</div>
  <div class="abs field" style="top:3289px;left:609px;width:358px">Nachname*</div>
  <div class="abs field" style="top:3339px;left:231px;width:359px">E-Mail*</div>
  <div class="abs field" style="top:3339px;left:609px;width:358px">Telefon</div>
  <div class="abs field" style="top:3389px;left:231px;width:736px">Betreff*</div>
  <div class="abs" style="top:3389px;left:420px;font-size:17px;font-weight:700;color:var(--ink)">Vereinbaren Sie einen Termin mit mir</div>
  <svg class="abs" style="top:3397px;left:938px" width="18" height="12" viewBox="0 0 18 12"><path d="M2 3l7 6 7-6" stroke="#2b2b2b" stroke-width="2.5" fill="none"/></svg>
  <div class="abs field" style="top:3440px;left:231px;width:736px">Ihre Nachricht*</div>
  <p class="abs note">Maximale Zeichenanzahl 1000.<br>1000 verbleibende Zeichen.</p>
  <div class="abs" style="top:3539px;left:231px;width:737px;height:1px;background:var(--line)"></div>
  <div class="abs send">SENDEN
    <svg width="26" height="20" viewBox="0 0 26 20"><path d="M1 10h23M15 1l9 9-9 9" stroke="#fff" stroke-width="2" fill="none"/></svg>
  </div>
</section>

<footer>
  <div class="abs footer"></div>
  <div class="abs footer-col" style="left:231px"><b>LM-Hausbau GmbH</b><br>Am Lindenhang 12<br>79901 Wiesenau<br>Tel. 07390-4827-0</div>
  <div class="abs footer-col" style="left:423px"><b>Unsere Bürozeiten sind:</b><br>Mo. bis Fr. von 08:30 Uhr bis 12:30 Uhr<br>Mo. bis Do. von 13:30 Uhr bis 18:00 Uhr<br>Freitag von 13:30 Uhr bis 16:00 Uhr<br>sowie nach Vereinbarung</div>
  <div class="abs footer-col" style="left:905px">Sitemap<br>Impressum<br>Datenschutz</div>
</footer>

</body>
</html>
```